realtor require a flyer to market a unit in prime district singapore

This flyer for the sale of "The Valmorelle" is to be distributed to high class district in PRIME homes in singapore. It has to be elegant but eye catching. It must also contain the following detail

1) 1605sqft
2) $2.4 mil with room for negotiation
3) Owner migrating
4) 3 + utility room
5) Desmond Kuah
6) 83527406
7) CEA no. 4718293B

In Singapore the marketing law is pretty strict hence, the following information must also be shown but may be in fine line

1) OKU Homefield network Pte Ltd with LOGO
2) Estate Agency License L5817406M

Target Market(s)

High network owners who has only that 1 sec to to catch their attention

Industry/Entity Type

Marketing

Font styles to use
Serif

Requirements
Must have
• What is stated above
Nice to have
• Nice to have the works and layout nicely crafted out

```html
<!DOCTYPE html>
<html lang="en">
<head>
<meta charset="utf-8">
<title>The Valmorelle – Property Flyer</title>
<link rel="stylesheet" href="https://fonts.googleapis.com/css2?family=Montserrat:wght@400;500;600&family=Libre+Baskerville:wght@400;700&display=swap">
<style>
  :root {
    --page-bg: #e8e8e8;
    --paper: #ffffff;
    --navy: #24205e;
    --navy-deep: #1b1850;
    --frame: #4a4890;
    --accent-red: #d7182a;
    --ink: #222222;
    --ink-soft: #6a6a6a;
    --white: #ffffff;
    --footer-bg: #f1f1f1;
  }
  * { margin: 0; padding: 0; box-sizing: border-box; }
  html, body {
    width: 1200px; height: 806px; overflow: hidden;
    background: var(--page-bg);
    font-family: "Montserrat", Arial, sans-serif;
  }
  .flyer {
    position: absolute; left: 350px; top: 18px;
    width: 500px; height: 770px;
    background: var(--paper);
    box-shadow: 0 6px 24px rgba(0,0,0,0.18);
    overflow: hidden;
  }
  .hero {
    position: absolute; left: 0; top: 0; width: 500px; height: 316px;
    background:
      linear-gradient(180deg, #9fbfe0 0%, #dfe6ee 22%, #f4f4f4 45%, #c9ccd2 62%, #5f9fc9 72%, #2f7fb8 100%);
  }
  .hero-title {
    position: absolute; right: 14px; top: 242px;
    text-align: right; color: var(--white);
    font-family: "Libre Baskerville", Georgia, serif; font-weight: 400;
    text-shadow: 0 1px 3px rgba(0,0,0,0.35);
    line-height: 1.12;
  }
  .hero-title .line-one { display: block; font-size: 24px; }
  .hero-title .line-two { display: block; font-size: 18px; }
  .rule-red {
    position: absolute; left: 0; top: 316px; width: 500px; height: 8px;
    background: var(--accent-red);
  }
  .details {
    position: absolute; left: 0; top: 324px; width: 500px; height: 340px;
    background: linear-gradient(180deg, var(--navy-deep) 0%, var(--navy) 100%);
    color: var(--white);
  }
  .section-title {
    font-family: "Libre Baskerville", Georgia, serif;
    font-size: 14px; font-weight: 700; letter-spacing: 0.2px;
  }
  .about { position: absolute; left: 24px; top: 20px; width: 234px; }
  .about p {
    margin-top: 7px; font-size: 8.8px; line-height: 13.6px; text-align: justify;
  }
  .features { position: absolute; left: 24px; top: 190px; width: 234px; }
  .feature-list { list-style: none; margin-top: 8px; }
  .feature-list li {
    font-size: 12px; line-height: 24px; padding-left: 16px; position: relative;
    white-space: nowrap;
  }
  .feature-list li::before {
    content: ""; position: absolute; left: 2px; top: 10px;
    width: 5px; height: 5px; border-radius: 50%; background: var(--white);
  }
  .gallery {
    position: absolute; left: 272px; top: 28px;
    display: grid; grid-template-columns: 102px 102px; grid-template-rows: 124px 124px;
    gap: 8px;
  }
  .gallery-photo { border: 4px solid var(--frame); }
  .photo-living { background: linear-gradient(160deg, #e9e2d6 0%, #b9a18a 55%, #5a4538 100%); }
  .photo-dining { background: linear-gradient(160deg, #7f9e73 0%, #cfd7cb 50%, #8a7a6a 100%); }
  .photo-bedroom { background: linear-gradient(160deg, #efeae3 0%, #c58f52 55%, #7a5232 100%); }
  .photo-kitchen { background: linear-gradient(160deg, #f1ede6 0%, #c9b69d 55%, #3b332c 100%); }
  .bar-left, .bar-right {
    position: absolute; top: 330px; height: 10px; background: var(--accent-red);
  }
  .bar-left { left: 0; width: 140px; }
  .bar-right { right: 0; width: 132px; }
  .footer {
    position: absolute; left: 0; top: 664px; width: 500px; height: 106px;
    background: var(--footer-bg);
  }
  .brand {
    position: absolute; left: 30px; top: 32px;
    display: flex; align-items: center; gap: 6px;
  }
  .brand-mark { width: 16px; height: 16px; background: var(--accent-red); }
  .brand-name {
    font-family: "Montserrat", Arial, sans-serif; font-weight: 600;
    font-size: 24px; color: var(--accent-red); letter-spacing: 1px;
  }
  .company { position: absolute; left: 136px; top: 20px; width: 190px; }
  .company-url {
    font-size: 11px; font-weight: 500; letter-spacing: 2px; color: var(--ink);
  }
  .fine-print {
    margin-top: 8px; font-size: 5.6px; line-height: 7.6px; color: var(--ink-soft);
  }
  .agent-photo {
    position: absolute; left: 340px; top: 14px; width: 52px; height: 68px;
    background: linear-gradient(180deg, #e8e8e8 0%, #d6c6b8 45%, #2a2a30 80%, #1d1d22 100%);
  }
  .agent {
    position: absolute; left: 400px; top: 14px; width: 94px; color: var(--ink);
  }
  .agent-name {
    font-family: "Libre Baskerville", Georgia, serif; font-weight: 700; font-size: 9px;
    white-space: nowrap;
  }
  .agent-role { font-size: 6.5px; color: var(--ink-soft); margin-top: 3px; }
  .agent-contact { margin-top: 12px; font-size: 5.8px; line-height: 8.6px; color: var(--ink-soft); white-space: nowrap; }
</style>
</head>
<body>
  <main class="flyer">
    <div class="hero" role="img" aria-label="Condominium towers of The Valmorelle around a large blue swimming pool"></div>
    <h1 class="hero-title">
      <span class="line-one">The Dream Home</span>
      <span class="line-two">You are Looking for...</span>
    </h1>
    <div class="rule-red"></div>

    <section class="details">
      <div class="about">
        <h2 class="section-title">ABOUT THE PROPERTY</h2>
        <p>The Valmorelle. Lorem ipsum dolor sit amet, consectetur adipiscing elit. In sodales, nulla sit amet ultricies lobortis, arcu sapien rhoncus eros, eget dictum mi erat vitae arcu. Sed elementum ac enim sit amet semper. Donec est velit, porttitor ut tortor consequat, tempus imperdiet dolor. Sed suscipit, lectus ut imperdiet auctor. In sodales, nulla sit amet ultricies lobortis, arcu sapien rhoncus eros.</p>
      </div>
      <div class="features">
        <h2 class="section-title">PROPERTY FEATURES</h2>
        <ul class="feature-list">
          <li>1605 sqft</li>
          <li>$2.4 mil with room for negotiation</li>
          <li>Owner migrating</li>
          <li>3 + utility room</li>
        </ul>
      </div>
      <div class="gallery">
        <div class="gallery-photo photo-living" role="img" aria-label="Living room with sofas and ceiling fan"></div>
        <div class="gallery-photo photo-dining" role="img" aria-label="Glass-walled dining area with garden view"></div>
        <div class="gallery-photo photo-bedroom" role="img" aria-label="Bedroom with wooden built-in wardrobe"></div>
        <div class="gallery-photo photo-kitchen" role="img" aria-label="Dining room with dark table and chairs"></div>
      </div>
      <div class="bar-left"></div>
      <div class="bar-right"></div>
    </section>

    <footer class="footer">
      <div class="brand">
        <span class="brand-mark"></span>
        <span class="brand-name">OKU</span>
      </div>
      <div class="company">
        <div class="company-url">www.yourcompany.com</div>
        <p class="fine-print">Marketed by OKU Homefield network Pte Ltd. Estate Agency License L5817406M. Salesperson Desmond Kuah, CEA no. 4718293B. All information is believed accurate but not guaranteed. Viewing strictly by appointment only.</p>
      </div>
      <div class="agent-photo" role="img" aria-label="Portrait of the real estate broker"></div>
      <div class="agent">
        <div class="agent-name">Desmond Kuah</div>
        <div class="agent-role">Real Estate Broker</div>
        <div class="agent-contact">
          Phone: 83527406<br>
          Email: dk@yourcompany.com<br>
          Social: @dkuah
        </div>
      </div>
    </footer>
  </main>
</body>
</html>
```